The Quiet Meadow - a modern wellness brand

Looking for a modern, simple, and clean website for a virtual consulting firm focused on holistic wellness and sustainable living. Want a strong combo of text and photos (really shitty starts are available for reference on www.thequietmeadowhub.example and www.ginaposlund.example for reference - general idea is in the right direction, was too difficult to work through with the wordpress template and nothing laid out correctly)
Needs include:
- strong home / landing page
- ability to schedule (use calend.ly) on the site
- online shop / purchasing POS integration
- blog
-multiple 'services' pages
- about page
- contact page
(attached brand board images for brand style / reference)
Updates
Want more opportunity for designs and feedback
Target Market(s)
women and gay men aged 30-50
Coding
Coded - Design and coding required
Number of Pages Required
5+ page
Colors
Designer to choose only greyscale colors for use in the design.
Requirements
Must have
- the ability for me to update and manage through wordpress when things like pricing, or services change
Should not have
- complicated anything

```html
<!DOCTYPE html>
<html lang="en">
<head>
<meta charset="utf-8">
<title>The Quiet Meadow — Journal</title>
<link href="https://fonts.googleapis.com/css2?family=Gilda+Display&family=Montserrat:wght@400;500;600&display=swap" rel="stylesheet">
<style>
:root{
  --ink:#1f1f1f;
  --text:#4a4a4a;
  --muted:#8a8a8a;
  --rule:#d6d6d6;
  --paper:#ffffff;
  --footer:#262626;
  --footer-text:#c9c9c9;
  --button:#3e4a42;
  --accent:#b23a3a;
}
*{margin:0;padding:0;box-sizing:border-box}
html,body{width:1200px;height:3764px;overflow:hidden;background:var(--paper)}
body{position:relative;font-family:"Montserrat",sans-serif;color:var(--text);font-size:15px;line-height:1.65}
.serif{font-family:"Gilda Display",serif}
.abs{position:absolute}

/* header */
.site-header{position:absolute;top:0;left:0;width:1200px;height:112px;display:flex;align-items:center;padding:0 60px}
.brand{display:flex;align-items:center;gap:14px}
.brand-dot{width:58px;height:58px;border:1.5px solid var(--ink);border-radius:50%}
.brand-name{font-family:"Gilda Display",serif;font-size:22px;letter-spacing:3px;color:var(--ink)}
.main-nav{position:absolute;left:532px;top:50px;display:flex;gap:34px;font-size:11px;font-weight:600;letter-spacing:1.5px;color:var(--ink)}
.main-nav .current{border-bottom:2px solid var(--ink);padding-bottom:4px}
.header-icons{position:absolute;left:1018px;top:38px;display:flex;gap:20px;align-items:center}

/* hero */
.hero{position:absolute;top:112px;left:0;width:1200px;height:488px;background:linear-gradient(180deg,#8c8f92 0%,#b9b2a8 45%,#7c7a76 100%)}
.hero-shade{position:absolute;inset:0;background:rgba(30,30,30,.35)}
.hero-copy{position:absolute;left:0;width:1200px;top:260px;text-align:center;color:#fff}
.tag-label{display:inline-block;background:#5b5b5b;font-size:10px;font-weight:600;letter-spacing:1.5px;padding:4px 12px}
.hero-title{font-family:"Gilda Display",serif;font-size:42px;line-height:1.2;font-weight:400;margin:16px auto 0;width:780px}
.hero-meta{font-size:13px;margin-top:18px;opacity:.9}

/* article */
.article p{position:absolute;left:260px;width:680px;font-size:15px;line-height:1.68}
.dropcap{position:absolute;left:260px;top:660px;font-family:"Gilda Display",serif;font-size:84px;line-height:1;color:var(--ink)}
.section-heading{position:absolute;left:260px;top:922px;font-family:"Gilda Display",serif;font-size:30px;font-weight:400;color:var(--ink)}
.photo{position:absolute}

/* tags */
.tags{position:absolute;left:260px;top:2414px;display:flex;gap:12px}
.tags span{border:1px solid var(--ink);font-size:13px;padding:6px 12px;color:var(--ink)}
.rule{position:absolute;left:260px;width:680px;height:1px;background:var(--rule)}
.like{position:absolute;left:268px;top:2528px;width:50px;height:50px;border:1.5px solid var(--ink);border-radius:50%;display:flex;align-items:center;justify-content:center}
.prev-label{position:absolute;left:272px;top:2658px;font-size:12px;letter-spacing:1.5px;color:var(--ink);font-weight:500}
.prev-title{position:absolute;left:272px;top:2700px;font-family:"Gilda Display",serif;font-size:20px;line-height:1.3;color:var(--ink);width:420px}

/* comment form */
.comment-heading{position:absolute;left:260px;top:2900px;font-family:"Gilda Display",serif;font-size:36px;font-weight:400;color:var(--ink)}
.field{position:absolute;font-size:12px;color:var(--muted);border-bottom:1px solid var(--rule);padding-bottom:12px}
.consent{position:absolute;left:260px;top:3160px;display:flex;align-items:center;gap:12px;font-size:14px;color:var(--ink)}
.consent .box{width:16px;height:16px;border:1.5px solid var(--ink)}
.consent u{color:var(--ink)}
.submit{position:absolute;left:260px;top:3246px;width:216px;height:66px;background:var(--button);color:#fff;font-family:"Gilda Display",serif;font-size:18px;display:flex;align-items:center;justify-content:center}

/* footer */
.site-footer{position:absolute;top:3392px;left:0;width:1200px;height:372px;background:var(--footer);color:var(--footer-text)}
.footer-brand{position:absolute;left:116px;top:74px;display:flex;align-items:center;gap:12px}
.footer-brand .brand-dot{border-color:var(--footer-text);width:50px;height:50px}
.footer-brand .brand-name{color:#fff;font-size:19px}
.social{position:absolute;left:118px;top:146px;display:flex;gap:10px}
.social span{width:16px;height:16px;border-radius:50%;background:var(--footer-text)}
.newsletter-title{position:absolute;left:116px;top:180px;font-family:"Gilda Display",serif;font-size:28px;color:#fff}
.newsletter-input{position:absolute;left:116px;top:228px;width:240px;border-bottom:1px solid var(--footer-text);font-size:12px;padding:6px 0 8px 22px}
.newsletter-input::before{content:"";position:absolute;left:0;top:9px;width:12px;height:9px;border:1px solid var(--footer-text)}
.newsletter-arrow{position:absolute;left:340px;top:236px}
.footer-col{position:absolute;top:82px;font-size:13px;line-height:2.2}
.footer-col h4{font-family:"Gilda Display",serif;font-weight:400;font-size:15px;color:#fff;letter-spacing:1px;margin-bottom:10px}
.footer-bottom{position:absolute;top:328px;font-size:10px;color:var(--muted)}
</style>
</head>
<body>

<header class="site-header">
  <div class="brand"><span class="brand-dot"></span><span class="brand-name">THE QUIET MEADOW</span></div>
  <nav class="main-nav">
    <span class="current">HOME</span><span>OUR SERVICES</span><span>ABOUT US</span><span>SHOP</span><span>CONTACT US</span>
  </nav>
  <div class="header-icons">
    <svg width="22" height="24" viewBox="0 0 22 24" fill="none" stroke="#1f1f1f" stroke-width="1.6"><path d="M3 7h16l-1 15H4z"/><path d="M7 7V5a4 4 0 0 1 8 0v2"/><circle cx="18" cy="5" r="5" fill="#b23a3a" stroke="none"/></svg>
    <svg width="22" height="22" viewBox="0 0 22 22" fill="none" stroke="#1f1f1f" stroke-width="2"><circle cx="9" cy="9" r="7"/><path d="M14 14l6 6"/></svg>
    <svg width="24" height="24" viewBox="0 0 24 24" fill="#1f1f1f"><rect x="1" y="1" width="5" height="5"/><rect x="9.5" y="1" width="5" height="5"/><rect x="18" y="1" width="5" height="5"/><rect x="1" y="9.5" width="5" height="5"/><rect x="9.5" y="9.5" width="5" height="5"/><rect x="18" y="9.5" width="5" height="5"/><rect x="1" y="18" width="5" height="5"/><rect x="9.5" y="18" width="5" height="5"/><rect x="18" y="18" width="5" height="5"/></svg>
  </div>
</header>

<section class="hero" role="img" aria-label="Woman with long hair seen from behind, looking out over a calm sea">
  <div class="hero-shade"></div>
  <div class="hero-copy">
    <span class="tag-label">HEALTH</span>
    <h1 class="hero-title">Lorem ipsum dolor sit amet, consectetur adipiscing elit. Nec velit sapien</h1>
    <div class="hero-meta">May 12, 2022 &nbsp;|&nbsp; 0 Comments</div>
  </div>
</section>

<article class="article">
  <span class="dropcap">Q</span>
  <p style="top:656px;left:336px;width:604px">Proin faucibus nec mauris a sodales, sed elementum mi tincidunt. Sed eget viverra egestas nisi in consequat. Fusce sodales augue a accumsan. Cras sollicitudin, ipsum eget blandit pulvinar. Integer tincidunt. Cras dapibus. Vivamus elementum semper nisi. Aenean vulputate eleifend tellus. Aenean leo ligula, porttitor eu, consequat vitae, eleifend ac, enim.</p>
  <p style="top:790px">Sed ut perspiciatis, unde omnis iste natus error sit voluptatem accusantium doloremque laudantium, totam rem aperiam eaque ipsa, quae ab illo inventore veritatis et quasi architecto beatae vitae dicta sunt, explicabo.</p>

  <h2 class="section-heading">At vero eos et accusam</h2>
  <p style="top:976px">Sed ut perspiciatis, unde omnis iste natus error sit voluptatem accusantium doloremque laudantium, totam rem aperiam eaque ipsa, quae ab illo inventore veritatis et quasi architecto beatae vitae dicta sunt.</p>

  <div class="photo" style="left:132px;top:1088px;width:460px;height:304px;background:linear-gradient(180deg,#d9b89a 0%,#c78e72 40%,#6a5a55 70%,#3b3634 100%)" role="img" aria-label="Stacked pebbles on still water at sunset"></div>
  <div class="photo" style="left:608px;top:1088px;width:460px;height:304px;background:linear-gradient(135deg,#f4f2f0 0%,#eedcd6 50%,#e8c2b8 100%)" role="img" aria-label="Dropper bottle of oil surrounded by pink rose petals"></div>

  <p style="top:1424px">Ut perspiciatis, unde omnis iste natus error sit voluptatem accusantium doloremque laudantium, totam rem aperiam eaque ipsa, quae ab illo inventore veritatis et quasi architecto beatae vitae dicta sunt, explicabo.</p>
  <p style="top:1510px">Sed ut perspiciatis, unde omnis iste natus error sit voluptatem accusantium doloremque laudantium, totam rem aperiam eaque ipsa, quae ab illo inventore veritatis et quasi architecto beatae vitae dicta sunt, explicabo.</p>
  <p style="top:1594px">Lorem ipsum dolor sit amet, consectetur adipiscing elit, sed do eiusmod tempor incididunt ut labore et dolore magna aliqua. Ut enim ad minim veniam, quis nostrud exercitation ullamco laboris nisi ut aliquip ex ea commodo consequat. Duis aute irure dolor in reprehenderit. Lorem ipsum dolor sit amet, consectetur adipiscing elit.</p>

  <div class="photo" style="left:132px;top:1740px;width:936px;height:420px;background:radial-gradient(ellipse at 50% 55%,#6f7379 0%,#9aa3ab 40%,#c4ccd3 100%)" role="img" aria-label="Balanced stack of smooth stones rising from rippling water"></div>

  <p style="top:2216px">Lorem ipsum dolor sit amet, consectetur adipiscing elit, sed do eiusmod tempor incididunt ut labore et dolore magna aliqua. Ut enim ad minim veniam, quis nostrud exercitation ullamco laboris nisi ut aliquip ex ea commodo consequat. Duis aute irure dolor in reprehenderit. Lorem ipsum dolor sit amet, consectetur adipiscing elit.</p>
  <p style="top:2322px">Etiam vitae leo et diam pellentesque porta. Sed eleifend ultricies risus, vel rutrum erat commodo ut. Praesent finibus congue euismod. Nullam scelerisque massa vel augue placerat, a tempor sem egestas. Curabitur placerat finibus lacus.</p>

  <div class="tags"><span>Wellness</span><span>Holistic</span></div>
</article>

<div class="rule" style="top:2500px"></div>
<div class="like"><svg width="22" height="20" viewBox="0 0 22 20" fill="none" stroke="#1f1f1f" stroke-width="1.6"><path d="M11 18S2 12.5 2 6.5A4.5 4.5 0 0 1 11 4.5 4.5 4.5 0 0 1 20 6.5C20 12.5 11 18 11 18z"/></svg></div>
<div class="rule" style="top:2604px"></div>

<div class="prev-label"><svg width="10" height="12" viewBox="0 0 10 12" fill="none" stroke="#1f1f1f" stroke-width="1.6" style="margin-right:14px;vertical-align:-1px"><path d="M8 1L2 6l6 5"/></svg>PREVIOUS</div>
<div class="prev-title">Lorem ipsum dolor sit amet, consectetur adipiscing elit. Nec velit sapien</div>
<div class="rule" style="top:2818px"></div>

<h2 class="comment-heading">Leave a comment</h2>
<div class="field" style="left:260px;top:2990px;width:330px">Your name*</div>
<div class="field" style="left:604px;top:2990px;width:336px">Your email*</div>
<div class="field" style="left:260px;top:3062px;width:680px;padding-bottom:40px">Your comment*</div>
<div class="consent"><span class="box"></span><span>I agree that my submitted data is being <u>collected and stored</u>. *</span></div>
<div class="submit">Leave comment</div>

<footer class="site-footer">
  <div class="footer-brand"><span class="brand-dot"></span><span class="brand-name">THE QUIET MEADOW</span></div>
  <div class="social"><span></span><span></span><span></span><span></span></div>
  <div class="newsletter-title">Newsletter Signup</div>
  <div class="newsletter-input">Enter your email address</div>
  <svg class="newsletter-arrow" width="14" height="10" viewBox="0 0 14 10" fill="none" stroke="#c9c9c9" stroke-width="1.4"><path d="M0 5h12M8 1l4 4-4 4"/></svg>

  <div class="footer-col" style="left:732px">
    <h4>QUICK LINKS</h4>
    About Us<br>Blog<br>Contact Us<br>Shop
  </div>
  <div class="footer-col" style="left:912px">
    <h4>OUR SERVICE</h4>
    The Quiet Meadow<br>Executive &amp; Individual Coaching<br>The Meadow Podcast<br>The Meadow Blog
  </div>

  <div class="footer-bottom" style="left:116px">© Legal | Privacy Policy</div>
  <div class="footer-bottom" style="left:876px">Terms &amp; Conditions | Privacy Policy</div>
</footer>

</body>
</html>
```